Business Card for IT company

I need a high tech looking business card using our logo. I prefer something clean and modern.

Target Market(s)

Buyers of IT hardware and software, IT Techies who are key influencers

Industry/Entity Type

Business

```html
<!DOCTYPE html>
<html lang="en">
<head>
<meta charset="utf-8">
<title>Norvale Consulting – Business Card</title>
<link rel="stylesheet" href="https://fonts.googleapis.com/css2?family=PT+Sans:wght@400&display=swap">
<style>
  :root {
    --card-light: #e2e2e2;
    --card-mid: #b4b4b4;
    --card-dark: #8c8c8c;
    --ink: #343432;
    --card-width: 1200px;
    --card-height: 694px;
  }

  html, body {
    margin: 0;
    padding: 0;
    width: var(--card-width);
    height: var(--card-height);
    overflow: hidden;
  }

  .business-card {
    position: relative;
    width: var(--card-width);
    height: var(--card-height);
    background: linear-gradient(35deg, var(--card-light) 0%, var(--card-mid) 50%, var(--card-dark) 100%);
    font-family: "PT Sans", sans-serif;
    color: var(--ink);
    overflow: hidden;
  }

  .brand {
    position: absolute;
    top: 40px;
    right: 47px;
    text-align: right;
    font-weight: 400;
    color: var(--ink);
  }

  .brand-name {
    display: block;
    font-size: 150px;
    line-height: 1;
    letter-spacing: 0.01em;
  }

  .brand-tagline {
    display: block;
    margin-top: 22px;
    margin-right: -0.62em;
    font-size: 40px;
    line-height: 1;
    letter-spacing: 0.62em;
  }

  .contact {
    position: absolute;
    left: 72px;
    top: 398px;
    margin: 0;
    font-size: 45px;
    line-height: 62px;
    font-weight: 400;
  }

  .contact-line {
    display: block;
  }
</style>
</head>
<body>
  <main class="business-card">
    <div class="brand">
      <span class="brand-name">NORVALE</span>
      <span class="brand-tagline">CONSULTING</span>
    </div>

    <address class="contact" style="font-style: normal;">
      <span class="contact-line">Your Name Your Position</span>
      <span class="contact-line">Phone xxx.xxx.xxxx</span>
      <span class="contact-line">Email address@xx.com</span>
      <span class="contact-line">web xx.com</span>
    </address>
  </main>
</body>
</html>
```